Bright Harbor Works Buisness Cards

Provide a business card layout

Paul Wexford
PO Box 742
Norfolk MA 02318
paul@thwexample.com

Industry/Entity Type

Business

Font styles to use
Serif

Colors
f04a50

```html
<!DOCTYPE html>
<html lang="en">
<head>
<meta charset="utf-8">
<title>Bright Harbor Works – Business Card</title>
<link rel="stylesheet" href="https://fonts.googleapis.com/css2?family=Noto+Serif:wght@400;700&display=swap">
<style>
  :root {
    --backdrop: #d4d4d4;
    --card-white: #ffffff;
    --brand-red: #8e1116;
    --brand-gold: #e8a537;
    --ink: #141414;
    --panel-dark: #0e0e0e;
    --panel-mid: #1d1d1d;
    --text-light: #f4f4f4;
  }
  * { margin: 0; padding: 0; box-sizing: border-box; }
  html, body {
    width: 1200px;
    height: 900px;
    overflow: hidden;
    background: var(--backdrop);
    font-family: "Noto Serif", Georgia, serif;
  }
  .business-card {
    position: absolute;
    left: 150px;
    top: 170px;
    width: 900px;
    height: 560px;
    border-radius: 36px;
    overflow: hidden;
    background: var(--card-white);
    box-shadow: 0 18px 40px rgba(0, 0, 0, 0.22);
    display: flex;
    flex-direction: column;
  }
  .card-brand {
    height: 270px;
    flex: none;
    display: flex;
    align-items: center;
    justify-content: center;
    gap: 22px;
  }
  .brand-dot {
    width: 44px;
    height: 44px;
    border-radius: 50%;
    background: var(--brand-red);
  }
  .brand-name {
    font-size: 54px;
    font-weight: 700;
    color: var(--ink);
    letter-spacing: 1px;
  }
  .accent-band {
    height: 14px;
    flex: none;
    background: var(--brand-red);
  }
  .card-contact {
    flex: 1;
    background: linear-gradient(180deg, var(--panel-mid), var(--panel-dark));
    padding: 30px 56px 48px;
  }
  .person-name {
    font-size: 34px;
    font-weight: 700;
    line-height: 46px;
    color: var(--brand-gold);
    margin-bottom: 22px;
  }
  .contact-list { list-style: none; }
  .contact-item {
    display: flex;
    align-items: center;
    gap: 16px;
    font-size: 27px;
    line-height: 38px;
    color: var(--text-light);
  }
  .contact-icon {
    width: 30px;
    height: 30px;
    fill: var(--brand-red);
    flex: none;
  }
  .contact-icon .envelope-fold {
    fill: none;
    stroke: var(--panel-dark);
    stroke-width: 1.6;
  }
</style>
</head>
<body>
  <article class="business-card">
    <header class="card-brand">
      <span class="brand-dot"></span>
      <span class="brand-name">Bright Harbor Works</span>
    </header>
    <div class="accent-band"></div>
    <section class="card-contact">
      <h1 class="person-name">Paul Wexford</h1>
      <ul class="contact-list">
        <li class="contact-item">
          <svg class="contact-icon" viewBox="0 0 24 24" aria-hidden="true">
            <path d="M6.6 10.8c1.4 2.8 3.8 5.2 6.6 6.6l2.2-2.2c.3-.3.7-.4 1-.2 1.1.4 2.3.6 3.6.6.6 0 1 .4 1 1V20c0 .6-.4 1-1 1C10.6 21 3 13.4 3 4c0-.6.4-1 1-1h3.5c.6 0 1 .4 1 1 0 1.3.2 2.5.6 3.6.1.3 0 .7-.2 1z"/>
          </svg>
          <span>555 014 2736</span>
        </li>
        <li class="contact-item">
          <svg class="contact-icon" viewBox="0 0 24 24" aria-hidden="true">
            <rect x="2" y="5" width="20" height="14" rx="1.5"/>
            <polyline class="envelope-fold" points="2.5,6 12,13 21.5,6"/>
          </svg>
          <span>paul@thwexample.com</span>
        </li>
        <li class="contact-item">
          <svg class="contact-icon" viewBox="0 0 24 24" aria-hidden="true">
            <path d="M12 3l10 9h-3v9h-5v-6h-4v6H5v-9H2z"/>
          </svg>
          <span>PO Box 742, Norfolk MA 02318</span>
        </li>
      </ul>
    </section>
  </article>
</body>
</html>
```